Info Graphic about Maple Orchard Restaurant

This info graphic should detail all releavent details about Maple Orchard, such as opening hours, accepted payment methods, home delivery areas etc. please refer attached word document for details.

Also attached a pdf with old info graphic.

IMPORTANT:. Given there is lot of text, I expect the designer to make this interesting. This will be printed in A1 and also A4
Also, I need this in both Portrait and landscape designs.

Industry/Entity Type

Hospitality

Font styles to use
Serif
Sans Serif
Decorative
Script
Other font styles liked:
• I let designer choose

Colors

Designer to choose colors to be used in the design.

Requirements
Must have
• Refer attached word doc
Nice to have
• Refer attached word doc
Should not have
• Refer attached word doc

```html
<!DOCTYPE html>
<html lang="en">
<head>
<meta charset="utf-8">
<title>Maple Orchard Indian Restaurant – Info</title>
<link href="https://fonts.googleapis.com/css2?family=Almendra:wght@700&family=Bebas+Neue&family=Oswald:wght@300&family=Roboto:wght@400;700&display=swap" rel="stylesheet">
<style>
:root{
  --orange:#f7901e;
  --panel:#1b1b1b;
  --red:#c1272d;
  --tick:#b8bb2c;
  --cross:#e0201e;
  --white:#ffffff;
  --ink:#1a1a1a;
  --pepper:#d8532a;
}
*{margin:0;padding:0;box-sizing:border-box}
html,body{width:849px;height:1200px;overflow:hidden;background:#fff}
.poster{position:relative;width:849px;height:1200px;overflow:hidden;font-family:'Roboto',sans-serif;color:var(--white)}
.backdrop{position:absolute;inset:0;background:radial-gradient(ellipse at 50% 55%,#c2642a 0%,#9a4a22 45%,#6e3a26 75%,#e9e2dc 100%)}
.header{position:absolute;left:0;top:0;width:849px;height:172px}
.header svg{position:absolute;inset:0}
.title{position:absolute;left:0;width:849px;top:30px;text-align:center;font-family:'Almendra',serif;font-weight:700;font-size:37px;color:var(--red);line-height:1;white-space:nowrap}
.url{position:absolute;left:0;width:849px;top:78px;text-align:center;font-size:23px;letter-spacing:5px;color:var(--ink)}
.header-art{position:absolute;top:22px;width:64px;height:104px;border-radius:10px;background:var(--pepper)}
.header-art.left{left:34px}.header-art.right{left:751px}
.panel{position:absolute;left:58px;top:210px;width:733px;height:927px;background:var(--panel);border-radius:22px}
.abs{position:absolute}
.heading{position:absolute;font-family:'Bebas Neue',sans-serif;font-size:33px;color:var(--orange);text-align:center;line-height:1;letter-spacing:.3px}
.hours{position:absolute;left:80px;top:286px;width:326px;border-collapse:collapse;font-size:17px}
.hours td,.hours th{border:1.5px solid var(--white);padding:2px 10px;text-align:left;vertical-align:middle;line-height:1.2}
.hours th{height:31px;font-weight:700}
.hours td{height:55px}
.hours thead th:first-child{border-right:none}
.hours thead th:nth-child(2){border-left:none;border-right:none}
.hours thead th:nth-child(3){border-left:none}
.note{font-family:'Oswald',sans-serif;font-weight:300;font-variant:small-caps;font-size:16px;line-height:24px}
.suburbs{position:absolute;font-size:17px;line-height:28.4px;list-style:none}
.body{font-size:17px;line-height:26px}
.contact{position:absolute;left:450px;font-size:18px;display:flex;align-items:center;gap:12px}
.contact .ico{width:32px;height:32px;border-radius:50%;background:var(--orange);display:flex;align-items:center;justify-content:center}
.pay{position:absolute;left:442px;top:508px;width:326px;border-collapse:collapse;font-weight:700;font-size:18px}
.pay td{border:1.5px solid var(--white);height:31.5px;padding:0 6px}
.pay td svg{float:right}
.services{position:absolute;left:460px;top:816px;list-style:none;font-size:23px;line-height:27.4px}
.services li::before{content:"";display:inline-block;width:7px;height:7px;border-radius:50%;background:var(--white);margin-right:23px;vertical-align:middle}
.logo{position:absolute;top:1007px;width:70px;height:70px;border:3px solid var(--orange);border-radius:50%;display:flex;align-items:center;justify-content:center;font-family:'Bebas Neue',sans-serif;font-size:24px;color:var(--orange)}
</style>
</head>
<body>
<div class="poster">
  <div class="backdrop" role="img" aria-label="Close-up photo of an Indian curry dish"></div>

  <div class="header">
    <svg width="849" height="172" viewBox="0 0 849 172"><polygon points="0,0 849,0 849,128 424,170 0,128" fill="#f7901e"/></svg>
    <div class="header-art left" role="img" aria-label="Illustration of a bunch of chillies"></div>
    <div class="header-art right" role="img" aria-label="Illustration of a bunch of chillies"></div>
    <h1 class="title">Maple Orchard Indian Restaurant</h1>
    <div class="url">www.mapleorchard.com.au</div>
  </div>

  <div class="panel"></div>

  <h2 class="heading" style="left:80px;width:326px;top:236px">Opening Hours</h2>
  <table class="hours">
    <thead><tr><th style="width:116px"></th><th style="width:108px">Morning</th><th>Evening</th></tr></thead>
    <tbody>
      <tr><td>Monday to Friday</td><td>11:30AM-<br>2:30PM</td><td>5:00PM-<br>9:00PM</td></tr>
      <tr><td>Saturday to Sunday</td><td>10:30AM-<br>2:30PM</td><td>5:00PM-<br>9:00PM</td></tr>
    </tbody>
  </table>
  <p class="abs note" style="left:88px;top:432px;width:310px">Dinner Buffet is available only from Mon-Thu from 5:30PM-8:30PM</p>

  <h2 class="heading" style="left:80px;width:326px;top:497px;line-height:41px">We deliver to the<br>follwing suburbs</h2>
  <ul class="suburbs" style="left:104px;top:580px">
    <li>Beldon</li><li>Craigie</li><li>Darch</li><li>Duncraig</li><li>Edgewater</li><li>Greenwood</li><li>Woodvale</li>
  </ul>
  <ul class="suburbs" style="left:325px;top:580px">
    <li>Hocking</li><li>Kingsley</li><li>Madeley</li><li>Padbury</li><li>Pearsall</li><li>Wangara</li>
  </ul>

  <h2 class="heading" style="left:60px;width:366px;top:800px">BYO (Bring Your Own)</h2>
  <p class="abs body" style="left:60px;width:366px;top:840px;text-align:center;font-size:18px">Wine only - Corkage per bottle apply</p>
  <h2 class="heading" style="left:60px;width:366px;top:884px">Outside food is not allowed!</h2>
  <h2 class="heading" style="left:60px;width:366px;top:941px">Discount Vouchers</h2>
  <p class="abs body" style="left:81px;top:976px;width:340px">We accept leisure book vouchers and maple orchard supplied discount vouchers.</p>
  <p class="abs body" style="left:81px;top:1043px;width:340px">Leisure vouchers are eligible only for dine-in</p>

  <h2 class="heading" style="left:442px;width:330px;top:236px">Booking/Orders Contact</h2>
  <div class="contact" style="top:292px"><span class="ico"><svg width="18" height="18" viewBox="0 0 24 24"><path d="M6.6 10.8a15 15 0 0 0 6.6 6.6l2.2-2.2c.3-.3.7-.4 1-.2 1.1.4 2.3.6 3.6.6.6 0 1 .4 1 1V20c0 .6-.4 1-1 1A17 17 0 0 1 3 4c0-.6.4-1 1-1h3.5c.6 0 1 .4 1 1 0 1.3.2 2.5.6 3.6.1.3 0 .7-.2 1z" fill="#1b1b1b"/></svg></span>08 9555 0142</div>
  <div class="contact" style="top:338px"><span class="ico"><svg width="20" height="14" viewBox="0 0 20 14"><rect x="1" y="1" width="18" height="12" fill="none" stroke="#1b1b1b" stroke-width="2"/><path d="M1 1l9 7 9-7" fill="none" stroke="#1b1b1b" stroke-width="2"/></svg></span>admin@mapleorchard.com.au</div>
  <div class="contact" style="top:384px"><span class="ico"><svg width="18" height="18" viewBox="0 0 20 20" fill="none" stroke="#1b1b1b" stroke-width="1.6"><circle cx="10" cy="10" r="8"/><ellipse cx="10" cy="10" rx="3.5" ry="8"/><path d="M2 10h16M3.5 6h13M3.5 14h13"/></svg></span>www.mapleorchard.com.au</div>

  <h2 class="heading" style="left:442px;width:330px;top:462px">Payment Methods</h2>
  <table class="pay">
    <tr><td>Cash<svg width="30" height="24" viewBox="0 0 30 24"><path d="M3 13l8 8L27 3" fill="none" stroke="#b8bb2c" stroke-width="5"/></svg></td></tr>
    <tr><td>TapPay<svg width="30" height="24" viewBox="0 0 30 24"><path d="M3 13l8 8L27 3" fill="none" stroke="#b8bb2c" stroke-width="5"/></svg></td></tr>
    <tr><td>Northcard/Sterling<svg width="30" height="24" viewBox="0 0 30 24"><path d="M3 13l8 8L27 3" fill="none" stroke="#b8bb2c" stroke-width="5"/></svg></td></tr>
    <tr><td>Debit/Credit<svg width="30" height="24" viewBox="0 0 30 24"><path d="M3 13l8 8L27 3" fill="none" stroke="#b8bb2c" stroke-width="5"/></svg></td></tr>
    <tr><td>Amberex*<svg width="30" height="24" viewBox="0 0 30 24"><path d="M3 13l8 8L27 3" fill="none" stroke="#b8bb2c" stroke-width="5"/></svg></td></tr>
    <tr><td>JKP*<svg width="30" height="24" viewBox="0 0 30 24"><path d="M3 13l8 8L27 3" fill="none" stroke="#b8bb2c" stroke-width="5"/></svg></td></tr>
    <tr><td>Dinewell<svg width="30" height="24" viewBox="0 0 30 24"><path d="M9 4l12 16M21 4L9 20" stroke="#e0201e" stroke-width="4"/></svg></td></tr>
  </table>
  <p class="abs note" style="left:448px;top:734px">* Surcharge of 2.8% apply</p>

  <h2 class="heading" style="left:442px;width:296px;top:780px">Services</h2>
  <ul class="services">
    <li>Functions/Parties</li><li>Bulk cooking</li><li>Special orders</li><li>Business meetings</li><li>Seminars/Presentations</li>
  </ul>

  <div class="logo" style="left:447px">Logo</div>
  <div class="logo" style="left:529px">Logo</div>
  <div class="logo" style="left:610px">Logo</div>
  <div class="logo" style="left:691px">Logo</div>
</div>
</body>
</html>
```